Tovesca Website

I need a website for a startup company that provides GIS (Geographic Information Services) staffing and products for local cities. Current website is www.tovescagroup.com

```html
<!DOCTYPE html>
<html lang="en">
<head>
<meta charset="utf-8">
<title>Tovesca Group</title>
<link href="https://fonts.googleapis.com/css2?family=Poppins:wght@400;500;600&display=swap" rel="stylesheet">
<style>
:root{
  --ink:#111;
  --accent:#0a7aa8;
  --card-light:#ececec;
  --card-dark:#666;
  --form-bg:#dad7d9;
  --footer-bg:#3f3f3f;
  --rule:#555;
  --white:#fff;
}
*{margin:0;padding:0;box-sizing:border-box}
html,body{width:1200px;height:3450px;overflow:hidden;background:var(--white)}
body{font-family:'Poppins',sans-serif;color:var(--ink);position:relative}
.abs{position:absolute}
.site-header{position:absolute;left:0;top:0;width:1200px;height:83px;background:var(--white)}
.brand{left:50px;top:20px;font-size:32px;font-weight:600}
.nav a{position:absolute;top:28px;font-size:20px;color:var(--ink);text-decoration:none}
.nav a.active{color:var(--accent)}
.hero{left:0;top:83px;width:1200px;height:704px;background:linear-gradient(110deg,#7a8a6e 0%,#4e5a52 35%,#2c3138 60%,#5a4a42 80%,#1f2226 100%)}
.hero-box{left:43px;top:264px;width:440px;height:309px;background:rgba(45,45,45,.88);color:var(--white);padding:40px 29px}
.hero-box .eyebrow{font-size:20px}
.hero-box h1{font-size:41px;font-weight:600;line-height:40px;margin-top:8px}
.hero-box p{font-size:16.5px;line-height:24px;margin-top:18px;width:340px}
.btn{display:block;background:var(--accent);color:var(--white);font-size:16px;text-align:center;text-decoration:none}
.hero-box .btn{position:absolute;left:29px;top:229px;width:138px;height:42px;line-height:42px}
.section-title{font-size:33px;font-weight:400;text-align:center}
.card{width:338px;height:434px;background:var(--card-light)}
.card .photo{height:215px;background:linear-gradient(135deg,#8a9ca8,#5e6f7a 50%,#3d4a52)}
.card h3{font-size:25px;font-weight:500;margin:12px 0 0 30px}
.card ul{list-style:none;margin:14px 0 0 30px}
.card li{font-size:16.5px;height:40px;display:flex;align-items:center;gap:12px}
.card .etc{font-size:16.5px;margin:-4px 0 0 58px}
.card.dark{background:var(--card-dark);color:var(--white)}
.about-title{left:54px;top:1585px;font-size:33px;font-weight:400}
.about-text{left:55px;top:1662px;width:480px;font-size:16.5px;line-height:32px}
.band{left:0;top:2066px;width:1200px;height:440px;background:linear-gradient(180deg,#5b5048 0%,#4a5560 40%,#6c7783 70%,var(--form-bg) 100%)}
.contact-bg{left:0;top:2506px;width:1200px;height:536px;background:var(--form-bg)}
.field{background:var(--white);font-size:20px;color:#444;padding:10px 10px}
.footer{left:0;top:3042px;width:1200px;height:363px;background:var(--footer-bg);color:var(--white)}
.footer .name{left:164px;top:100px;font-size:33px;font-weight:400}
.footer .blurb{left:164px;top:150px;width:400px;font-size:16.5px;line-height:32px}
.footer h4{font-size:22px;font-weight:400}
.footer .links a{display:block;color:var(--white);text-decoration:none;font-size:14.5px;height:32px}
.footer .addr{font-size:14.5px;line-height:31px}
.legal{left:0;top:3405px;width:1200px;height:45px;text-align:center;line-height:45px;font-size:16.5px}
</style>
</head>
<body>
<header class="site-header">
  <div class="abs brand">Tovesca Group</div>
  <nav class="nav">
    <a class="active" href="#" style="left:730px">Home</a>
    <a href="#" style="left:811px">Service</a>
    <a href="#" style="left:905px">About us</a>
    <a href="#" style="left:1020px">Contact us</a>
  </nav>
</header>

<section class="abs hero" role="img" aria-label="GIS analyst with glasses pointing a pen at a city map on a monitor"></section>
<div class="abs hero-box">
  <div class="eyebrow">Tovesca Group</div>
  <h1>We Make GIS Work For You</h1>
  <p>We are an innovative team of geospatial experts with 25 years of</p>
  <a class="btn" href="#">Contact Us</a>
</div>

<h2 class="abs section-title" style="left:0;top:856px;width:1232px">Our Services</h2>
<svg class="abs" style="left:563px;top:904px" width="106" height="18" viewBox="0 0 106 18"><line x1="0" y1="9" x2="106" y2="9" stroke="#555" stroke-width="2"/><rect x="48" y="3" width="9" height="9" fill="#555" transform="rotate(45 52.5 9)"/></svg>

<article class="abs card" style="left:43px;top:1003px">
  <div class="photo" role="img" aria-label="Consultant on the phone holding a map beside a row of yellow survey instruments"></div>
  <h3>GIS Consulting</h3>
  <ul>
    <li><svg width="14" height="14"><rect x="3" y="3" width="8" height="8" fill="var(--accent)" transform="rotate(45 7 7)"/></svg>GIS analysis</li>
    <li><svg width="14" height="14"><rect x="3" y="3" width="8" height="8" fill="var(--accent)" transform="rotate(45 7 7)"/></svg>Demographics</li>
    <li><svg width="14" height="14"><rect x="3" y="3" width="8" height="8" fill="var(--accent)" transform="rotate(45 7 7)"/></svg>Map products</li>
  </ul>
  <div class="etc">. . . . . . . etc</div>
</article>
<article class="abs card dark" style="left:421px;top:1003px">
  <div class="photo" role="img" aria-label="Hands holding a tablet showing a map"></div>
  <h3>GIS Applications</h3>
  <ul>
    <li><svg width="14" height="14"><rect x="3" y="3" width="8" height="8" fill="#fff" transform="rotate(45 7 7)"/></svg>MapCore Online</li>
    <li><svg width="14" height="14"><rect x="3" y="3" width="8" height="8" fill="#fff" transform="rotate(45 7 7)"/></svg>MapCore Enterprise</li>
    <li><svg width="14" height="14"><rect x="3" y="3" width="8" height="8" fill="#fff" transform="rotate(45 7 7)"/></svg>Dashboards</li>
  </ul>
  <div class="etc">. . . . . . . etc</div>
</article>
<article class="abs card" style="left:799px;top:1003px">
  <div class="photo" role="img" aria-label="Analyst touching a glowing blue city map on a screen"></div>
  <h3>Spatial Data Solutions</h3>
  <ul>
    <li><svg width="14" height="14"><rect x="3" y="3" width="8" height="8" fill="var(--accent)" transform="rotate(45 7 7)"/></svg>Spatial data cleanup</li>
    <li><svg width="14" height="14"><rect x="3" y="3" width="8" height="8" fill="var(--accent)" transform="rotate(45 7 7)"/></svg>GIS data model design/review</li>
    <li><svg width="14" height="14"><rect x="3" y="3" width="8" height="8" fill="var(--accent)" transform="rotate(45 7 7)"/></svg>Integrating with other system</li>
  </ul>
  <div class="etc">. . . . . . . etc</div>
</article>

<svg class="abs" style="left:563px;top:1498px" width="74" height="8"><rect x="0" y="1" width="15" height="5" fill="#b5a8a8"/><rect x="29" y="1" width="15" height="5" fill="#555"/><rect x="58" y="1" width="15" height="5" fill="#b5a8a8"/></svg>

<h2 class="abs about-title">About us</h2>
<svg class="abs" style="left:56px;top:1630px" width="100" height="16"><line x1="4" y1="8" x2="100" y2="8" stroke="#555" stroke-width="3"/><rect x="3" y="4" width="8" height="8" fill="#555" transform="rotate(45 7 8)"/></svg>
<p class="abs about-text">It is a long established fact that a reader will be distracted by the readable content of a page when looking at its layout. The point of using Lorem Ipsum is that it has a more-or-less normal distribution of letters, as opposed to using 'Content here, content here', making it look like readable English</p>
<a class="abs btn" href="#" style="left:52px;top:1871px;width:124px;height:40px;line-height:40px">Read More</a>

<svg class="abs" style="left:640px;top:1540px" width="460" height="490" viewBox="640 1540 460 490">
  <defs><linearGradient id="aboutPhoto" x1="0" y1="0" x2="0" y2="1"><stop offset="0" stop-color="#3a4a5e"/><stop offset=".5" stop-color="#4f7a95"/><stop offset="1" stop-color="#6d9bb0"/></linearGradient></defs>
  <polygon points="655,1795 870,2013 1085,1785 870,1575" fill="var(--accent)"/>
  <polygon points="870,1553 1085,1768 870,1983 653,1768" fill="url(#aboutPhoto)" role="img" aria-label="Planner leaning over an illuminated 3D city model"/>
</svg>

<section class="abs band" role="img" aria-label="Two analysts working at monitors displaying city maps"></section>
<div class="abs contact-bg"></div>
<h2 class="abs section-title" style="left:0;top:2555px;width:1200px">Contact Us</h2>
<svg class="abs" style="left:541px;top:2600px" width="106" height="18"><line x1="0" y1="9" x2="106" y2="9" stroke="#555" stroke-width="2"/><rect x="48" y="3" width="9" height="9" fill="#555" transform="rotate(45 52.5 9)"/></svg>
<form>
  <div class="abs field" style="left:292px;top:2673px;width:278px;height:49px">Name</div>
  <div class="abs field" style="left:621px;top:2673px;width:279px;height:49px">Email</div>
  <div class="abs field" style="left:292px;top:2753px;width:278px;height:49px">Phone Number</div>
  <div class="abs field" style="left:621px;top:2753px;width:279px;height:49px">Contact</div>
  <div class="abs field" style="left:292px;top:2830px;width:608px;height:85px">Message</div>
  <div class="abs btn" style="left:519px;top:2942px;width:124px;height:41px;line-height:41px;font-size:19px;font-weight:500">SEND</div>
</form>

<footer class="abs footer">
  <div class="abs name">Tovesca Group, LLC</div>
  <p class="abs blurb">Lorem Ipsum is simply dummy text of the printing and typesetting industry. Lorem Ipsum has been the industry's standard</p>
  <h4 class="abs" style="left:620px;top:92px">Quick Links</h4>
  <nav class="abs links" style="left:629px;top:140px">
    <a href="#">Home</a><a href="#">About Us</a><a href="#">Service</a><a href="#">Contact Us</a>
  </nav>
  <h4 class="abs" style="left:815px;top:92px">Address</h4>
  <svg class="abs" style="left:810px;top:144px" width="14" height="18" viewBox="0 0 14 18"><path d="M7 1a6 6 0 0 0-6 6c0 4.5 6 10 6 10s6-5.5 6-10a6 6 0 0 0-6-6z" fill="none" stroke="#fff" stroke-width="2"/><circle cx="7" cy="7" r="2" fill="#fff"/></svg>
  <div class="abs addr" style="left:830px;top:136px">4480 N. Alder Ave. #210<br>Brookfield, CA 90410</div>
</footer>
<div class="abs legal">Tovesca Group @Reserved by 2024</div>
</body>
</html>
```